Club sale for moms — 3 static banners

Toddla is the largest daily deal site for moms, kids and babies in Russia, which provides offers with discounts up to 70%.
We need 3 banners for our flash sale, all banners must be on a white background, all must be static and be in 2 versions, so when you hover over banner the picture changes. Banners' style should differ from other banners which refer to deals (like bimbly's banners "Invite a friend, earn $20", they are attached).
Purpose: filling the empty space on the main page in case of absence of the necessary number of deals' banners. The example of our main page is attached.
1st static banner:
474px × 308px
text: Пригласите друга — получите бонус на следующую покупку!
That text means: Invite a friend and get a bonus for shopping.
After clicking on that banner a client will go to the site section "Invites".
The text means: Invite a friend and get a bonus for shopping.
2nd static banner:
308px × 199px
Text: Доставка по всей России. Оплата при получении.
After clicking on that banner a client will go to the site section about delivery.
The text means: Delivery all over Russia, pay on getting.
3rd static banner:
308px × 199px
Text:
Гарантия лучшей цены!
The text means:
Best price guarantee
Target Market(s)
moms
Industry/Entity Type
Club
Look and feel
Each slider illustrates characteristics of the customer's brand and the style your logo design should communicate.

```html
<!DOCTYPE html>
<html lang="ru">
<head>
<meta charset="utf-8">
<title>Toddla — баннеры клубной распродажи</title>
<link rel="stylesheet" href="https://fonts.googleapis.com/css2?family=PT+Sans:wght@400;700&display=swap">
<style>
  :root {
    --stage: #5b5659;
    --card: #ffffff;
    --magenta: #c2257a;
    --magenta-dark: #9c165f;
    --magenta-light: #e0529b;
    --ink-grey: #6a6668;
    --photo-top: #c9d3dc;
    --photo-mid: #8ea3b8;
    --photo-bottom: #5d7590;
    --pastel-a: #f4e66e;
    --pastel-b: #b9e3f3;
    --pastel-c: #f6b3d6;
    --pastel-d: #c9efb0;
  }
  * { box-sizing: border-box; margin: 0; padding: 0; }
  html, body { width: 1200px; height: 900px; overflow: hidden; }
  body {
    background: var(--stage);
    font-family: "PT Sans", "Myriad Pro", sans-serif;
    position: relative;
  }
  .banner {
    position: absolute;
    background: var(--card);
    overflow: hidden;
  }

  /* Invite banner */
  .banner--invite { left: 52px; top: 97px; width: 589px; height: 713px; }
  .invite__title {
    position: absolute; left: 40px; top: 30px;
    font-size: 60px; font-weight: 400; color: var(--magenta);
    line-height: 1; white-space: nowrap;
  }
  .invite__text {
    position: absolute; left: 40px; top: 113px;
    font-size: 35px; font-weight: 400; color: var(--ink-grey); line-height: 45px;
  }
  .invite__photo {
    position: absolute; left: 225px; top: 210px; width: 364px; height: 503px;
    background: linear-gradient(180deg, var(--photo-top) 0%, var(--photo-mid) 45%, var(--photo-bottom) 100%);
  }

  /* Price guarantee banner */
  .banner--price { left: 676px; top: 139px; width: 463px; height: 299px; }
  .price__seal { position: absolute; left: 76px; top: 10px; width: 312px; height: 280px; }
  .price__text {
    position: absolute; left: 0; right: 0; top: 84px;
    text-align: center; color: #fff; font-weight: 400;
  }
  .price__line-small { display: block; font-size: 44px; line-height: 44px; }
  .price__line-big { display: block; font-size: 58px; line-height: 50px; }

  /* Delivery banner */
  .banner--delivery { left: 676px; top: 474px; width: 463px; height: 299px; }
  .delivery__map {
    position: absolute; left: 20px; top: 14px; width: 426px; height: 278px;
    opacity: 0.55;
    background:
      radial-gradient(circle at 20% 25%, var(--pastel-b) 0 18%, transparent 30%),
      radial-gradient(circle at 55% 15%, var(--pastel-c) 0 15%, transparent 28%),
      radial-gradient(circle at 80% 45%, var(--pastel-a) 0 18%, transparent 32%),
      radial-gradient(circle at 40% 70%, var(--pastel-d) 0 20%, transparent 34%),
      radial-gradient(circle at 75% 80%, var(--pastel-b) 0 14%, transparent 28%);
    border-radius: 40px 60px 30px 50px;
  }
  .delivery__title {
    position: absolute; left: 29px; top: 80px;
    font-size: 50px; font-weight: 400; color: var(--magenta); line-height: 63px;
    white-space: nowrap;
  }
  .delivery__note {
    position: absolute; left: 31px; top: 214px;
    font-size: 27px; font-weight: 400; color: var(--ink-grey);
  }
  .delivery__icon { position: absolute; left: 359px; top: 76px; width: 44px; height: 50px; }
</style>
</head>
<body>

<section class="banner banner--invite">
  <h1 class="invite__title">Пригласите друга</h1>
  <p class="invite__text">получите бонус<br>на следующую<br>покупку!</p>
  <div class="invite__photo" role="img" aria-label="Фотография: два смеющихся мальчика обнимаются"></div>
</section>

<section class="banner banner--price">
  <svg class="price__seal" viewBox="0 0 312 280" aria-hidden="true">
    <defs>
      <radialGradient id="sealFill" cx="45%" cy="40%" r="65%">
        <stop offset="0" stop-color="var(--magenta-light)"/>
        <stop offset="0.7" stop-color="var(--magenta)"/>
        <stop offset="1" stop-color="var(--magenta-dark)"/>
      </radialGradient>
    </defs>
    <ellipse cx="156" cy="142" rx="152" ry="136" fill="var(--magenta-dark)"/>
    <ellipse cx="156" cy="138" rx="148" ry="130" fill="url(#sealFill)"/>
    <ellipse cx="156" cy="140" rx="112" ry="100" fill="none" stroke="var(--magenta-dark)" stroke-width="6" opacity="0.6"/>
  </svg>
  <p class="price__text">
    <span class="price__line-small">Гарантия</span>
    <span class="price__line-big">лучшей<br>цены!</span>
  </p>
</section>

<section class="banner banner--delivery">
  <div class="delivery__map" role="img" aria-label="Иллюстрация: пастельная цветная карта регионов"></div>
  <svg class="delivery__icon" viewBox="0 0 42 48" aria-hidden="true" fill="none" stroke="#6a6668" stroke-width="3">
    <rect x="4" y="3" width="34" height="36" rx="8"/>
    <line x1="4" y1="22" x2="38" y2="22"/>
    <line x1="21" y1="3" x2="21" y2="22"/>
    <circle cx="12" cy="31" r="2.5" fill="#6a6668"/>
    <circle cx="30" cy="31" r="2.5" fill="#6a6668"/>
    <line x1="10" y1="39" x2="8" y2="46"/>
    <line x1="32" y1="39" x2="34" y2="46"/>
  </svg>
  <h2 class="delivery__title">Доставка по<br>всей России</h2>
  <p class="delivery__note">Оплата при получении</p>
</section>

</body>
</html>
```